TELVORIQ HOA Portal Site for Public

Clean up and organize current website; need website to look good and functional; this is a HOA (homeowner association management) website where homeowners can login and pay their bill, general information about a HOA, monthly newsletter page.
Competitors:
https://plumbrivet.com/
https://duskorrahill.com/
https://www.qxlivingspan.com/nevada
http://www.bpt-hoa.com/

Target Market(s)

homeowners

Industry/Entity Type

Real Estate

Coding

Coded - Design and coding required

Number of Pages Required

5+ page

Font styles to use
Serif

Colors
0292cd
33a6d7
e667a6
e34297

Requirements
Must have
• login to pay
• services page
• contact us
• order resale package
Nice to have
• page why an HOA would contract us

```html
<!DOCTYPE html>
<html lang="en">
<head>
<meta charset="utf-8">
<title>TELVORIQ HOA</title>
<link rel="stylesheet" href="https://fonts.googleapis.com/css2?family=Roboto:wght@400;500;700;900&family=Lato:wght@400;700&display=swap">
<style>
:root{
  --blue:#0292cd;
  --blue-light:#33a6d7;
  --pink:#e34297;
  --pink-light:#e667a6;
  --ink:#111111;
  --text:#555555;
  --tint:#e5f3fa;
  --dark:#2e2f31;
  --footer:#111214;
}
*{box-sizing:border-box;margin:0;padding:0}
html,body{width:1200px;height:3435px;overflow:hidden}
body{position:relative;background:#fff;font-family:'Lato',sans-serif;color:var(--text)}
.abs{position:absolute}
h1,h2,h3,.btn,.logo{font-family:'Roboto',sans-serif}
.accent{color:var(--pink)}
.btn{position:absolute;display:flex;align-items:center;justify-content:center;background:var(--blue);color:#fff;font-weight:700;font-size:15px;border-radius:2px;text-decoration:none}

/* header */
.site-header{position:absolute;left:0;top:0;width:1200px;height:60px;background:var(--blue)}
.logo{position:absolute;left:163px;top:16px;font-family:'Lato',sans-serif;font-weight:700;font-size:22px;color:#fff;letter-spacing:.2px}
.main-nav{position:absolute;top:22px;left:0;font-size:12px;color:#fff}
.main-nav span{position:absolute;white-space:nowrap}
.main-nav .active{font-weight:700}
.btn-login{left:957px;top:11px;width:82px;height:37px;background:var(--pink);font-size:15px}

/* hero */
.hero{position:absolute;left:0;top:60px;width:1200px;height:600px;background:linear-gradient(180deg,#5d5e62 0%,#6b4a35 35%,#3e3a36 55%,#2f5a6e 75%,#1f3f52 100%)}
.hero-box{position:absolute;left:276px;top:191px;width:648px;height:337px;background:rgba(0,0,0,.55);border:1px solid rgba(255,255,255,.6);text-align:center;color:#fff}
.hero-box h1{margin-top:48px;font-size:46px;line-height:52px;font-weight:700;letter-spacing:.3px}
.hero-box p{margin:18px auto 0;width:490px;font-size:13px;line-height:21px}
.btn-hero{left:257px;top:239px;width:134px;height:44px;font-size:18px}
.hero-line{position:absolute;height:1px;background:rgba(255,255,255,.7)}

/* about */
.section-title{position:absolute;font-size:37px;font-weight:700;color:var(--ink)}
.body-copy{position:absolute;font-size:11.5px;line-height:19.5px;color:var(--text)}
.photo{position:absolute}
.about-frame{position:absolute;left:611px;top:708px;width:428px;height:283px;background:#fff;box-shadow:0 0 10px rgba(0,0,0,.18)}

/* offer */
.offer{position:absolute;left:0;top:1047px;width:1200px;height:390px;background:var(--tint)}

/* management */
.management{position:absolute;left:0;top:1437px;width:1200px;height:600px;background:linear-gradient(160deg,#3b3c3e,#232426 60%,#2b2c2e)}
.management h2{position:absolute;left:0;top:62px;width:1200px;text-align:center;font-size:37px;font-weight:700;color:#fff}
.card{position:absolute;top:154px;width:278px;height:374px;background:#fff;text-align:center}
.card .photo{left:0;top:0;width:278px;height:173px}
.card h3{position:absolute;top:190px;width:100%;font-size:19px;font-weight:500;color:var(--pink)}
.card p{position:absolute;top:218px;left:16px;width:246px;font-size:11.5px;line-height:19.5px}
.card .btn{left:90px;top:315px;width:98px;height:37px}

/* testimonials */
.testimonial-card{position:absolute;left:279px;top:2217px;width:642px;height:206px;background:#fff;border-radius:6px;box-shadow:0 0 10px rgba(0,0,0,.2)}
.quote-mark{position:absolute;font-family:'Roboto',sans-serif;font-weight:900;font-size:80px;color:#e2e2e2;line-height:1}
.dot{position:absolute;width:12px;height:12px;border:1px solid var(--pink);border-radius:50%}
.dot.on::after{content:"";position:absolute;left:2px;top:2px;width:6px;height:6px;border-radius:50%;background:var(--pink)}

/* contact */
.field{position:absolute;left:391px;width:418px;height:44px;border:1px solid #cfcfcf;border-radius:2px;font-size:11px;color:#888;padding:16px 10px}

/* newsletter */
.newsletter{position:absolute;left:0;top:3007px;width:1200px;height:90px;background:var(--blue)}
.newsletter h2{position:absolute;left:163px;top:28px;font-size:29px;font-weight:500;color:#fff}
.news-input{position:absolute;left:589px;top:22px;width:372px;height:46px;background:#fff;font-size:11px;color:#444;padding:17px 10px}
.news-send{position:absolute;left:961px;top:22px;width:48px;height:46px;background:#0e1620}

/* footer */
.site-footer{position:absolute;left:0;top:3097px;width:1200px;height:338px;background:var(--footer);color:#fff;text-align:center}
.footer-logo{position:absolute;left:0;top:48px;width:1200px;font-family:'Lato',sans-serif;font-weight:700;font-size:22px;color:var(--blue)}
.footer-nav{position:absolute;top:100px;left:0;font-size:12px}
.footer-nav span{position:absolute;white-space:nowrap}
.social{position:absolute;top:140px;width:36px;height:36px;border-radius:50%;background:#fff}
.footer-line{position:absolute;left:0;width:1200px;font-size:11.5px}
.footer-rule{position:absolute;left:161px;top:291px;width:878px;height:1px;background:#444}
</style>
</head>
<body>

<header class="site-header">
  <div class="logo">TELVORIQ HOA</div>
  <nav class="main-nav">
    <span style="left:484px">Home</span>
    <span style="left:550px" class="active">About Us</span>
    <span style="left:633px">Services</span>
    <span style="left:708px">Why Us</span>
    <span style="left:784px">Contact Us</span>
  </nav>
  <a class="btn btn-login">Login</a>
</header>

<section class="hero" role="img" aria-label="Photo of a lit timber lodge beside a reflecting pool at dusk">
  <div class="hero-line" style="left:230px;top:272px;width:82px"></div>
  <div class="hero-line" style="left:888px;top:272px;width:82px"></div>
  <div class="hero-box" style="top:131px">
    <h1>HOMEOWNER ASSOCIATION<br>MANAGEMENT</h1>
    <p>Lorem Ipsum is simply dummy text of the printing and typesetting industry. Lorem Ipsum has been the industry's standard dummy text ever since the 1500s</p>
    <a class="btn btn-hero">Contact Us</a>
  </div>
</section>

<section class="about">
  <h2 class="section-title" style="left:163px;top:704px">About <span class="accent">Us</span></h2>
  <p class="body-copy" style="left:163px;top:773px;width:428px">Lorem Ipsum is simply dummy text of the printing and typesetting industry. Lorem Ipsum has been the industry's standard dummy text ever since the 1500s, when an unknown printer took a galley of type and scrambled it to make a type specimen book.</p>
  <p class="body-copy" style="left:163px;top:870px;width:428px">It has survived not only five centuries, but also the leap into electronic typesetting, remaining essentially unchanged.</p>
  <a class="btn" style="left:161px;top:941px;width:113px;height:38px">Read More</a>
  <div class="about-frame">
    <div class="photo" role="img" aria-label="Photo of a smiling couple in front of their house and garden" style="left:12px;top:12px;width:404px;height:259px;background:linear-gradient(180deg,#d7dde3 0%,#9fb08e 45%,#6e8a4c 70%,#8a5a42 100%)"></div>
  </div>
</section>

<section class="offer">
  <div class="photo" role="img" aria-label="Illustration of cupped hands holding a small model house" style="left:60px;top:10px;width:470px;height:330px;background:radial-gradient(ellipse at center,#e8b79a 0%,#d9a184 45%,rgba(229,243,250,0) 72%)"></div>
  <h2 class="section-title" style="left:613px;top:45px">What We <span class="accent">Offer</span></h2>
  <p class="body-copy" style="left:613px;top:115px;width:425px">Accessible, licensed Association Managers<br>24 hour Web site access: online account information<br>24 hour emergency service<br>Provide monthly financial reports to the Board of Directors<br>Read, study and understand all governing documents of the Association.<br>Correspond with members in violation of the CC&amp;Rs, By-laws, Rules &amp; Regulations and report the status of all noncompliance to the Board of Directors in a timely manner.</p>
  <a class="btn" style="left:611px;top:290px;width:113px;height:37px">Read More</a>
</section>

<section class="management" role="region" aria-label="Roof texture backdrop">
  <h2>Homeowner Association <span class="accent">Management</span></h2>
  <div class="card" style="left:161px">
    <div class="photo" role="img" aria-label="Photo of a two-storey house at sunset" style="background:linear-gradient(180deg,#8b8fc4 0%,#c9a6c0 45%,#3c4770 70%,#59684a 100%)"></div>
    <h3>Our Services</h3>
    <p>Lorem Ipsum is simply dummy text of the printing and typesetting industry. Lorem Ipsum has been the industry's standard dummy text ever since the 1500s.</p>
    <a class="btn">View All</a>
  </div>
  <div class="card" style="left:461px">
    <div class="photo" role="img" aria-label="Photo of a group relaxing in a bright living room" style="background:linear-gradient(180deg,#e8e6e2 0%,#bdb9b1 50%,#4a4e44 100%)"></div>
    <h3>Why HOA?</h3>
    <p>Lorem Ipsum is simply dummy text of the printing and typesetting industry. Lorem Ipsum has been the industry's standard dummy text ever since the 1500s.</p>
    <a class="btn">Read More</a>
  </div>
  <div class="card" style="left:761px">
    <div class="photo" role="img" aria-label="Photo of house keys handed over between two people" style="background:linear-gradient(90deg,#b8323a 0%,#c74a4e 35%,#5e6a7a 60%,#d9c8b6 100%)"></div>
    <h3>Order Resale Package</h3>
    <p>Lorem Ipsum is simply dummy text of the printing and typesetting industry. Lorem Ipsum has been the industry's standard dummy text ever since the 1500s.</p>
    <a class="btn">Login</a>
  </div>
</section>

<section class="testimonials">
  <h2 class="section-title" style="left:0;top:2095px;width:1200px;text-align:center">Our <span class="accent">Testimonials</span></h2>
  <div class="dot" style="left:221px;top:2281px"></div>
  <div class="dot" style="left:221px;top:2303px"></div>
  <div class="dot on" style="left:221px;top:2326px"></div>
  <div class="dot" style="left:221px;top:2349px"></div>
  <div class="testimonial-card">
    <div class="quote-mark" style="left:15px;top:38px">&ldquo;</div>
    <div class="quote-mark" style="left:580px;top:128px">&rdquo;</div>
    <p style="position:absolute;left:0;top:49px;width:100%;text-align:center;font-family:'Roboto',sans-serif;font-weight:700;font-size:11.5px;color:var(--pink)">-Client Name</p>
    <p class="body-copy" style="left:48px;top:78px;width:546px;text-align:center">Lorem Ipsum is simply dummy text of the printing and typesetting industry. Lorem Ipsum has been the industry's standard dummy text ever since the 1500s, when an unknown printer took a galley of type and scrambled it to make a type specimen book.<br>It has survived not only five centuries, but also the leap into electronic typesetting, remaining essentially unchanged.</p>
  </div>
  <div class="abs" role="img" aria-label="Client portrait" style="left:562px;top:2181px;width:76px;height:76px;border-radius:50%;border:2px solid var(--pink);background:radial-gradient(circle at 50% 40%,#8a8f99,#2c2f36)"></div>
</section>

<section class="contact">
  <h2 class="section-title" style="left:0;top:2504px;width:1200px;text-align:center">Contact <span class="accent">Us</span></h2>
  <div class="field" style="top:2591px">Name:</div>
  <div class="field" style="top:2651px">Email:</div>
  <div class="field" style="top:2711px">Phone:</div>
  <div class="field" style="top:2771px;height:89px">Message:</div>
  <a class="btn" style="left:555px;top:2903px;width:90px;height:36px">Submit</a>
</section>

<section class="newsletter">
  <h2>Subscribe To Our Newsletter</h2>
  <div class="news-input">Enter Email:</div>
  <div class="news-send">
    <svg width="48" height="46" viewBox="0 0 48 46"><path d="M14 24 L34 14 L28 33 L24 26 Z M24 26 L34 14" fill="none" stroke="#fff" stroke-width="2" stroke-linejoin="round"/><path d="M14 24 L34 14 L24 26 Z" fill="#fff"/></svg>
  </div>
</section>

<footer class="site-footer">
  <div class="footer-logo">TELVORIQ HOA</div>
  <nav class="footer-nav">
    <span style="left:373px">Home</span>
    <span style="left:436px">About Us</span>
    <span style="left:517px">Services</span>
    <span style="left:591px">Why Us?</span>
    <span style="left:669px">Testimonials</span>
    <span style="left:766px">Contact Us</span>
  </nav>
  <div class="social" style="left:492px" aria-label="Social link"></div>
  <div class="social" style="left:552px" aria-label="Social link"></div>
  <div class="social" style="left:612px" aria-label="Social link"></div>
  <div class="social" style="left:672px" aria-label="Social link"></div>
  <p class="footer-line" style="top:200px;color:#bbb">101- Lorem ipsum is simply dummy text.</p>
  <p class="footer-line" style="top:224px">+91-000-000-0000</p>
  <p class="footer-line" style="top:250px;color:#999">info@telvoriqhoa.com</p>
  <div class="footer-rule"></div>
  <p class="footer-line" style="top:307px;font-size:11px;color:#ccc">Copyright © 2019 <span style="color:#fff">TELVORIQ HOA</span>. All Rights Reserved. Terms &amp; Conditions. | Privacy Policy.</p>
</footer>

</body>
</html>
```